KTR Associates Business Card

I would like to have a business card designed that uses my current logo and colors. I am not looking for anything to "out there" but can have a little fun so that it stands out.

I have a boutique consulting firm that specializes in strategic planning, change management, leadership development and innovation.

Industry/Entity Type

Leadership

Contact Information for Business Card

Marta Holloway
President
marta@ktr-associates-mail.com
919-555-0143

```html
<!DOCTYPE html>
<html lang="en">
<head>
<meta charset="utf-8">
<title>KTR Associates Business Card</title>
<link rel="stylesheet" href="https://fonts.googleapis.com/css2?family=Sorts+Mill+Goudy&family=Source+Sans+3:wght@400;600&display=swap">
<style>
  :root {
    --page: #ffffff;
    --ink: #231f20;
    --green: #2f7d3a;
    --green-deep: #3d8a3f;
    --lime: #c8d94a;
    --cream-top: #f1f3c8;
    --cream-bottom: #dfe596;
    --charcoal: #363436;
    --white: #ffffff;
    --url: #cfd653;
  }
  * { box-sizing: border-box; margin: 0; padding: 0; }
  html, body {
    width: 1200px; height: 1000px; overflow: hidden;
    background: var(--page);
  }
  .canvas { position: relative; width: 1200px; height: 1000px; }

  .card { position: absolute; overflow: hidden; }

  /* Company name block (set in the card's text font, one colour, one weight) */
  .company {
    position: absolute;
    font-family: "Source Sans 3", Arial, sans-serif;
    font-weight: 600;
    line-height: 1.05;
    letter-spacing: 1px;
  }

  /* Front card */
  .card--front {
    left: 30px; top: 30px; width: 870px; height: 500px; z-index: 2;
    background: linear-gradient(180deg, var(--cream-top) 0%, var(--cream-bottom) 100%);
    box-shadow: 0 2px 8px rgba(0,0,0,0.18);
  }
  .card--front .company {
    left: 90px; top: 110px; font-size: 62px; color: var(--ink);
  }

  .person { position: absolute; left: 442px; top: 112px; }
  .person__name {
    font-family: "Sorts Mill Goudy", Georgia, serif;
    font-size: 40px; color: var(--green); line-height: 1;
  }
  .person__title {
    font-family: "Source Sans 3", Arial, sans-serif; font-weight: 600;
    font-size: 19px; letter-spacing: 5px; color: var(--ink); margin-top: 12px;
  }
  .contact {
    position: absolute; left: 455px; top: 262px;
    font-family: "Source Sans 3", Arial, sans-serif; color: var(--ink);
  }
  .contact__phone {
    display: flex; align-items: center; gap: 10px;
    font-size: 29px; font-weight: 600; letter-spacing: 0.5px;
  }
  .contact__icon { width: 22px; height: 22px; }
  .contact__email { font-size: 26px; margin-top: 8px; }

  .brush-band {
    position: absolute; left: 0; bottom: 0; width: 870px; height: 170px;
  }

  /* Back card */
  .card--back {
    left: 330px; top: 500px; width: 840px; height: 465px; z-index: 1;
    background: var(--charcoal);
    box-shadow: 0 2px 8px rgba(0,0,0,0.25);
  }
  .card--back .company {
    right: 90px; top: 110px; font-size: 76px; color: var(--white); text-align: right;
  }
  .back-url {
    position: absolute; left: 380px; top: 368px;
    font-family: "Source Sans 3", Arial, sans-serif;
    font-size: 27px; color: var(--url); letter-spacing: 0.5px;
  }
</style>
</head>
<body>
<main class="canvas">

  <section class="card card--front" aria-label="Business card front">
    <p class="company">KTR<br>Associates</p>

    <div class="person">
      <p class="person__name">Marta Holloway</p>
      <p class="person__title">PRESIDENT</p>
    </div>

    <div class="contact">
      <p class="contact__phone">
        <svg class="contact__icon" viewBox="0 0 24 24" aria-hidden="true">
          <rect width="24" height="24" rx="4" fill="#2f7d3a"/>
          <path d="M8.2 5.5c.5-.3 1.1-.1 1.4.4l1.2 2.2c.3.5.1 1.1-.3 1.4l-1 .7c.7 1.6 2 2.9 3.6 3.6l.7-1c.3-.4.9-.6 1.4-.3l2.2 1.2c.5.3.7.9.4 1.4l-.8 1.3c-.4.6-1.1.9-1.8.8C10.4 16.5 7.5 13.6 6.8 8.8c-.1-.7.2-1.4.8-1.8z" fill="#ffffff"/>
        </svg>
        <span>919-555-0143</span>
      </p>
      <p class="contact__email">marta@ktr-associates-mail.com</p>
    </div>

    <svg class="brush-band" viewBox="0 0 870 170" role="img" aria-label="Decorative green brushstroke sweeping across the bottom of the card">
      <defs>
        <linearGradient id="bandFill" x1="0" y1="0" x2="1" y2="0">
          <stop offset="0" stop-color="#c8d94a"/>
          <stop offset="0.5" stop-color="#8fb53e"/>
          <stop offset="1" stop-color="#3d8a3f"/>
        </linearGradient>
      </defs>
      <path d="M0 150 C 220 80, 520 40, 870 20 L 870 70 C 560 90, 260 130, 0 170 Z" fill="url(#bandFill)" opacity="0.85"/>
    </svg>
  </section>

  <section class="card card--back" aria-label="Business card back">
    <p class="company">KTR<br>Associates</p>
    <p class="back-url">www.ktr-associates-mail.com</p>
  </section>

</main>
</body>
</html>
```